IT Consulting BrightwaveTecCo.com needs Simple and Neat WebDesigns

We are a IT consulting business, currently needing a logo and a neat website that looks simple and attractive. If could be creative enough to come up with something that follows these guidelines.
We are talking about 10-15 static pages here

1. Nice and Neat
2. Color consistancy
3. Latest menu bars
4. Easy cross navigation
5. Less Maintenance
6. Easy upgrades
Updates

Project Deadline Extended
Reason: new to this and getting familiar with the time I have onhand

Project Deadline Extended

Project Deadline Extended
Reason: I want to give more time to get good quality

Project Deadline Extended

Project Deadline Extended
Reason: inviting more designs

Target Market(s)

IT services and consulting - should look very very professional and elegant.

Industry/Entity Type

Business

Requirements
Must have
• I would like to receive the best designs for our website
Nice to have
• Design a good logo to go with the website

```html
<!DOCTYPE html>
<html lang="en">
<head>
<meta charset="utf-8">
<title>BrightwaveTec – IT Consulting</title>
<link href="https://fonts.googleapis.com/css2?family=Arimo:wght@400;700&display=swap" rel="stylesheet">
<style>
:root{
  --night:#0d0f12;
  --panel-grey:#e6e6e6;
  --paper:#ffffff;
  --ink:#1a1a1a;
  --body:#3a3a3a;
  --brand-blue:#3aa0d8;
  --link-blue:#2c6fb8;
  --footer:#222325;
  --footer-deep:#161719;
  --rule:#d4d4d4;
  --ok:#4c9a2a;
  --bad:#c0392b;
}
*{box-sizing:border-box;margin:0;padding:0}
html,body{width:825px;height:1200px;overflow:hidden}
body{position:relative;background:var(--footer);font-family:Arimo,Arial,sans-serif;color:var(--body);font-size:9px;line-height:1.5}
.abs{position:absolute}

.masthead{left:0;top:0;width:825px;height:360px;background:radial-gradient(ellipse at 50% 20%,#2a3036 0%,var(--night) 70%)}
.brand{left:97px;top:34px;display:flex;align-items:center;gap:10px}
.brand-dot{width:56px;height:56px;border-radius:50%;background:var(--brand-blue)}
.brand-name{font-size:30px;font-weight:700;color:#ffffff;letter-spacing:-.5px}
.support{left:625px;top:30px;color:#fff;font-size:8px;line-height:1.6;display:flex;gap:8px}
.support-icon{width:16px;height:16px;background:#e9b820;border-radius:2px;margin-top:2px}
.main-nav{left:418px;top:70px;display:flex}
.main-nav a{display:block;color:#e8e8e8;text-decoration:none;font-size:9px;padding:0 10px;height:35px;line-height:38px;border-right:1px solid #2e3236}
.main-nav a.active{background:#1f4a5c;border-top:2px solid var(--brand-blue);color:#cfe8f4}

.hero-visual{left:150px;top:137px;width:170px;height:170px;border-radius:6px;background:linear-gradient(180deg,#3b3f44,#c9cccf)}
.hero-title{left:355px;top:128px;width:380px;color:#fff;font-size:25px;line-height:1.28;font-weight:400}
.hero-title span{color:var(--brand-blue)}
.hero-kicker{left:354px;top:208px;color:#fff;font-weight:700;font-size:9px;line-height:1.5;text-transform:uppercase}
.hero-text{left:354px;top:240px;width:385px;color:#8d939a;font-size:9px}
.btn{display:block;width:46px;height:15px;line-height:15px;text-align:center;background:linear-gradient(#e2e2e2,#b8b8b8);color:#555;border-radius:3px;font-size:7.5px;text-decoration:none}
.hero-more{left:635px;top:297px;width:60px;height:18px;line-height:18px;font-size:10px}
.arrow{top:205px}

.services{left:83px;top:340px;width:659px;height:215px;background:var(--panel-grey)}
.services-tab{left:250px;top:325px;width:325px;height:25px;background:var(--panel-grey);clip-path:polygon(7% 0,93% 0,100% 100%,0 100%)}
.dots{left:378px;top:332px;width:66px;height:13px;border-radius:7px;background:#1d1f22;display:flex;align-items:center;justify-content:center;gap:5px}
.dots i{width:5px;height:5px;border-radius:50%;background:#555}
.dots i:first-child{background:var(--brand-blue)}
.service{top:378px}
.service-art{width:120px;height:58px;border:1px solid #bbb}
.service h3{font-size:9px;color:var(--ink);margin:12px 0 2px;text-transform:uppercase}
.service p{font-size:8px;line-height:12.2px;color:#333}
.mini{position:absolute;top:150px;font-size:6px;background:#fff;border:1px solid #ccc;padding:1px 5px;color:#777}
.col-rule{top:395px;width:1px;height:140px;background:#cfcfcf}

.content{left:83px;top:553px;width:659px;height:440px;background:var(--paper);border-radius:0 0 8px 8px;border-top:2px dotted #c9c9c9}
h2{font-size:12.5px;color:var(--ink);font-weight:400;line-height:1.2}
h2 span{color:var(--brand-blue)}
.copy{font-size:8px;line-height:12.6px;color:#333;text-align:justify}
.rule{height:1px;background:var(--rule)}
.why-item{font-size:8px;color:#333;white-space:nowrap;display:flex;gap:8px;align-items:center;line-height:12px}
.why-item b{color:#1e6fb3;font-size:11px}
.feature-icon{width:22px;height:24px;border-radius:2px}
.blue-sub{color:var(--link-blue);font-weight:700;font-size:8px}
.news-input{left:495px;top:918px;width:195px;height:22px;background:#1c1c1c;border-radius:3px;display:flex;align-items:center;justify-content:space-between;padding:0 3px 0 10px;color:#888;font-size:7px}
.news-input span{background:#d8d8d8;color:#111;font-weight:700;font-size:8px;padding:2px 6px;border-radius:2px}
.msg{font-size:7.5px;display:flex;gap:6px;align-items:center}

.foot-col h4{color:#fff;font-size:9px;text-transform:uppercase;margin-bottom:12px}
.foot-col p,.foot-col li{color:#8e8e8e;font-size:7px;line-height:1.7}
.foot-col ul{list-style:none}
.foot-col li:before{content:"";display:inline-block;width:4px;height:4px;border-radius:50%;background:#aaa;margin-right:8px;vertical-align:middle}
.quote{font-style:italic}
.bottom-bar{left:0;top:1140px;width:825px;height:60px;background:var(--footer-deep)}
.social{top:1163px;width:20px;height:20px;border-radius:2px}
.seal{left:680px;top:1147px;width:46px;height:46px;border-radius:50%;background:linear-gradient(#555,#2a2a2a)}
</style>
</head>
<body>

<header class="abs masthead"></header>
<div class="abs brand"><div class="brand-dot"></div><div class="brand-name">BrightwaveTec</div></div>
<div class="abs support"><div class="support-icon"></div><div>Click here to live Support<br>Toll Free <b>1-800-555-0142</b></div></div>
<nav class="abs main-nav"><a href="#">Home</a><a href="#" class="active">About Us</a><a href="#">Product</a><a href="#">Services</a><a href="#">Solution</a><a href="#">Contact Us</a></nav>

<div class="abs hero-visual" role="img" aria-label="Desktop monitor showing the company name"></div>
<h1 class="abs hero-title">Brightwave<span>Tec</span> will make sure your website works for you...</h1>
<p class="abs hero-kicker">Delivering world class data<br>integration solution</p>
<p class="abs hero-text">Fusce vehicula dignissim ligula. Vestibulum sit amet neque eu neque suscipit consequat quis vel risus. Ut enim ad minim veniam, quis nostrud exercitation ullamco laboris nisi ut aliquip ex ea commodo consequat. Duis aute irure dolor in reprehenderit in voluptate velit esse cillum dolore eu fugiat nulla pariatur.</p>
<a class="abs btn hero-more" href="#">Read more</a>
<svg class="abs arrow" style="left:84px" width="20" height="34" viewBox="0 0 20 34"><path d="M18 2 3 17l15 15" fill="none" stroke="#3d4247" stroke-width="4"/></svg>
<svg class="abs arrow" style="left:722px" width="20" height="34" viewBox="0 0 20 34"><path d="M2 2l15 15L2 32" fill="none" stroke="#3d4247" stroke-width="4"/></svg>

<div class="abs services-tab"></div>
<section class="abs services"></section>
<div class="abs dots"><i></i><i></i><i></i></div>
<div class="abs col-rule" style="left:302px"></div>
<div class="abs col-rule" style="left:528px"></div>

<article class="abs service" style="left:99px;width:168px">
  <div class="service-art" role="img" aria-label="Hand resting on a computer mouse" style="background:linear-gradient(135deg,#d9a088,#8a3f2a)"></div>
  <h3>Services</h3>
  <p>BrightwaveTec will work with you to maximise the efficiency of your systems and processes and provide fully managed teams or individuals to ensure the successful delivery of your project.</p>
  <a class="mini" style="left:0">MORE INFO</a>
</article>
<article class="abs service" style="left:341px;width:160px">
  <div class="service-art" role="img" aria-label="Coloured jigsaw puzzle pieces" style="background:linear-gradient(135deg,#c02a6a,#9fc03a 55%,#3a7ad0)"></div>
  <h3>Solution</h3>
  <p>BrightwaveTec's experts will work in partnership with you and with our best of breed technology and offshore partners to deliver solutions that are cost effective, fit for purpose and highly scalable.</p>
  <a class="mini" style="left:4px">MORE INFO</a>
</article>
<article class="abs service" style="left:554px;width:176px">
  <div class="service-art" role="img" aria-label="Stacked coloured product boxes" style="background:linear-gradient(135deg,#2f6fc0,#f0a030 60%,#e04030)"></div>
  <h3>Product</h3>
  <p>BrightwaveTec's experts will work in partnership with you and with our best of breed technology and offshore partners to deliver solutions that are cost effective, fit for purpose and highly scalable.</p>
  <a class="mini" style="left:16px">MORE INFO</a>
</article>

<main class="abs content"></main>

<h2 class="abs" style="left:97px;top:580px">Welcome to <span>BrightwaveTec</span></h2>
<p class="abs copy" style="left:97px;top:608px;width:306px">Group of individuals who had passion for data warehouse and with great reputation and integrity. With over eighteen years of industry experience we are building an organization, BrightwaveTec, from ground-up based on solid fundamentals, trust and commitment to provide quality service across various verticals. We believe that a reputation as an honest and reliable business is the recipe for success. While others seek to profit by cutting corners, or recommending unnecessary services to customers, BrightwaveTec believe that a good reputation and consistent service will reap bigger profits in the long run.</p>
<a class="abs btn" style="left:357px;top:716px">Read more</a>
<div class="abs rule" style="left:97px;top:740px;width:306px"></div>
<h2 class="abs" style="left:97px;top:750px">Why Choose Us?</h2>
<div class="abs why-item" style="left:97px;top:774px"><b>&#10140;</b>Sed congue, dui vel tristique mollis.</div>
<div class="abs why-item" style="left:276px;top:774px"><b>&#10140;</b>Sed congue, dui vel tristique</div>
<div class="abs why-item" style="left:97px;top:794px"><b>&#10140;</b>Morbi eget sem. Nam mollis.</div>
<div class="abs why-item" style="left:276px;top:794px"><b>&#10140;</b>mollis.</div>
<div class="abs why-item" style="left:97px;top:813px"><b>&#10140;</b>Donec sed velit ut tellus fermentum.</div>
<div class="abs why-item" style="left:276px;top:813px"><b>&#10140;</b>Morbi eget sem. Nam mollis.</div>
<div class="abs rule" style="left:97px;top:840px;width:306px"></div>
<h2 class="abs" style="left:97px;top:852px">What We Do</h2>
<p class="abs copy" style="left:97px;top:873px;width:306px">Duis aute irure dolor in reprehenderit in voluptate velit esse cillum dolore eu fugiat nulla pariatur. Excepteur sint occaecat cupidatat non proident, sunt in culpa qui officia deserunt mollit anim id est laborum.<br>Ut enim ad minim veniam, quis nostrud exercitation ullamco laboris nisi ut aliquip ex ea commodo consequat. Duis aute irure dolor in reprehenderit in voluptate velit esse cillum dolore eu fugiat nulla pariatur.</p>
<a class="abs btn" style="left:357px;top:962px">Read more</a>

<div class="abs feature-icon" style="left:455px;top:580px;background:linear-gradient(#f0a030,#2f7fd0)"></div>
<h2 class="abs" style="left:492px;top:585px">24h Technical Support</h2>
<p class="abs copy" style="left:452px;top:608px;width:278px">Fusce vehicula dignissim ligula.<br>Vestibulum sit amet neque eu neque suscipit consequat quis vel risus. Ut enim ad minim veniam, quis nostrud exercitation ullamco laboris nisi ut aliquip ex ea commodo consequat. Duis aute irure dolor in reprehenderit in voluptate velit esse cillum dolore eu fugiat nulla pariatur.</p>
<a class="abs btn" style="left:682px;top:682px">Read more</a>
<div class="abs rule" style="left:452px;top:706px;width:278px"></div>
<div class="abs feature-icon" style="left:454px;top:724px;background:linear-gradient(#f4f4f4,#9a9a9a)"></div>
<h2 class="abs" style="left:495px;top:728px">What we offer</h2>
<p class="abs blue-sub" style="left:452px;top:760px">Has been the industry's standard dummy.</p>
<p class="abs copy" style="left:452px;top:779px;width:278px">Simply dummy text of the printing and typesetting industry. Lorem Ipsum has been the industry's standard dummy text ever since this, when an unknown printer.<br>Lorem has been the industry's standard dummy text. Ever since this, when an unknown printer.</p>
<div class="abs rule" style="left:452px;top:855px;width:278px"></div>
<div class="abs feature-icon" style="left:453px;top:866px;background:linear-gradient(#e6eef7,#5f92c8)"></div>
<h2 class="abs" style="left:495px;top:864px">Subscribe to our newsletter.</h2>
<p class="abs copy" style="left:495px;top:881px;width:240px;text-align:left">Subscribe to our newsletter and get exclusive deals<br>you wont find anywhere else straight to your inbox!</p>
<div class="abs news-input">enter your email address<span>subscribe</span></div>
<div class="abs msg" style="left:497px;top:948px;color:var(--bad)"><svg width="10" height="10"><path d="M1 1l8 8M9 1 1 9" stroke="#c0392b" stroke-width="2.5"/></svg>please enter a valid email address</div>
<div class="abs msg" style="left:497px;top:964px;color:var(--ok)"><svg width="10" height="10"><path d="M1 5l3 3 5-7" fill="none" stroke="#4c9a2a" stroke-width="2.5"/></svg>thanks, your address has been added</div>

<footer>
  <div class="abs foot-col" style="left:97px;top:1028px;width:140px">
    <h4>What they say</h4>
    <p class="quote">“ Clear advice, fast delivery and a team that truly understands our systems and goals. ”</p>
    <p style="color:#ddd;font-weight:700;margin-top:6px">BY: DANA MERCER, IT MANAGER</p>
  </div>
  <div class="abs foot-col" style="left:263px;top:1028px;width:155px">
    <h4>About us</h4>
    <p>Vestibulum vehicula purus nec dui accumsan fermentum. Suspendisse potenti. Ut dapibus est id odio pretium blandit in eget leo. Aliquam erat volutpat. Curabitur blandit odio eget odio eleifend vel mattis augue convallis.</p>
  </div>
  <div class="abs foot-col" style="left:482px;top:1028px">
    <h4>Development</h4>
    <ul><li>Web Strategy</li><li>Web Applications</li><li>Flash Design</li><li>Hosting &amp; Domains</li></ul>
  </div>
  <div class="abs foot-col" style="left:596px;top:1028px;width:140px">
    <h4>Contact</h4>
    <p>Feel free to contact me or up below -<br>Address: 27 Harbor Lane, Westfield, 9<br>Telephone: +1-555-0188-2040<br>FAX: +1-555-0177<br>Others: +1-555-0166-3021<br>E-mail: mail@brightwavetec.com</p>
  </div>
</footer>
<div class="abs bottom-bar"></div>
<p class="abs" style="left:97px;top:1144px;color:#ccc;font-size:8px">Follow Us:</p>
<div class="abs social" style="left:97px;background:#3b5a9a" role="img" aria-label="Social profile link"></div>
<div class="abs social" style="left:129px;background:#3aa5d8" role="img" aria-label="Social profile link"></div>
<div class="abs social" style="left:160px;background:#e8782a" role="img" aria-label="Feed link"></div>
<p class="abs" style="left:525px;top:1160px;color:#888;font-size:7px;text-align:right;line-height:1.4">© Copyright BrightwaveTec . All Rights Reserved<br>Home | Contact | RSS</p>
<div class="abs seal"></div>

</body>
</html>
```